Upscale neighbourhood mail campaign requiring 3 postcard designs

I am looking for a series of 3 postcards to be designed. They all must have a common look to them to show they belong to the same company. We are a local real estate company that specializes in an area called Ashby Hollow. You can visit our website at www.ashbyhollowhomes.ca to have a peek. I have HD photos I can provide of the area, or include your own ideas/images. The post cards text will be provided and they will be sent as unaddressed admail, meaning there is no need to include areas for postage or mailing addresses. The final design should be clean, recognizable and professional. These cards must have visual impact on the recipients.

COPY for 3 POSTCARDs

POSTCARD 1

FRONT

(included Logo)

Get noticed.
Your home deserves it

BACK

We take finding Buyers for your home very seriously.

Through our unique, Ashby Hollow specific website, targeted digital marketing, EXCLUSIVE Buyer incentives and our featured listing promotion, your home is in front of the people that want to see it. People who WANT to live in Ashby Hollow.

Visit ashbyhollowhomes.ca to learn more about what we do so your home can GET NOTICED. Your home deserves it.

Colin Vasterby- PREC | Tallowin Realty LTD | 604-555-0193 | homes@vasterby.ca

This communication is not intended to cause or induce breach of an existing agency agreement. Although this information has been received from sources deemed reliable, we assume no responsibility for its accuracy and without offering advice, make this submission to prior sale or lease, change in price or terms, and withdrawal without notice

POSTCARD 2

FRONT

Logo

Get noticed.
Expect the best.

BACK

You deserve the best when it comes to the marketing and exposure of your home, which is why your neighbours choose ashbyhollowhomes.ca to sell their home. Our award winning results combined with our systematized approach to marketing makes selling your home with us a breeze. In addition, you have full access to our dedicated client concierge, in place to ensure your sale is stress free and an overall rewarding experience.

Visit ashbyhollowhomes.ca to learn more about what we do so your home can GET NOTICED. Expect the best.

POSTCARD 3

FRONT

Logo

Get noticed.
Rule the web

BACK

No one promotes your home more than ashbyhollowhomes.ca. Just try us. Type ashby hollow homes into any internet search browser and see for yourself. We advertise Ashby Hollow internationally, in all major Canadian Cities and locally to affluent Buyers who appreciate what Ashby Hollow has to offer. No one offers a more specific, targeted approach to getting your home sold.

Visit ashbyhollowhomes.ca to learn more about what we do so your home can GET NOTICED so you can rule the web.

Target Market(s)

Upscale neighbourhood in Surrey BC, Canada called Ashby Hollow

Industry/Entity Type

Real Estate

Other font styles liked:
• Lato

Colors

Designer to choose colors to be used in the design.

Requirements
Must have
• -Clean, impactful and professional looking card
• -Font- Lato
• -Provided Ashby Hollow Homes logo
• -Check www.ashbyhollowhomes.ca for complimentary color scheme
• -provided Ashby Hollow logo on the front
• -provided --CV logo, Tallowin Realty logo and medallion crest on the back
• -Disclaimer in small, low-key font/color - "This communication is not intended to cause or induce breach of an existing agency agreement. Although this information has been received from sources deemed reliable, we assume no responsibility for its accuracy and without offering advice, make this submission to prior sale or lease, change in price or terms, and withdrawal without notice"
Nice to have
• -bold images, not 100% necessary though (discretion of designer)
• -impactful front of postcard
Should not have
• -cartoon style drawings
• -areas for postage or mailing addresses (this will be sent as non addressed admail by the local postal courier)

```html
<!DOCTYPE html>
<html lang="en">
<head>
<meta charset="utf-8">
<title>Ashby Hollow Homes – Postcard 1</title>
<link rel="stylesheet" href="https://fonts.googleapis.com/css2?family=Lato:wght@400;700;900&display=swap">
<style>
  :root {
    --olive: #5b6a2e;
    --olive-deep: #4a5724;
    --ink: #2b2b2b;
    --card: #ffffff;
    --backdrop: #e9e9e9;
    --sky: #9fc0e4;
    --lawn: #6f9a3c;
    --muted: #d9dccb;
  }
  * { box-sizing: border-box; margin: 0; padding: 0; }
  html, body { width: 1200px; height: 960px; overflow: hidden; }
  body {
    background: var(--backdrop);
    font-family: "Lato", sans-serif;
    color: var(--ink);
    position: relative;
  }
  .postcard {
    position: absolute;
    left: 260px;
    width: 680px;
    height: 453px;
    background: var(--card);
    box-shadow: 0 2px 10px rgba(0,0,0,0.12);
    overflow: hidden;
  }
  .postcard--front { top: 17px; }
  .postcard--back { top: 490px; }

  .brand {
    display: flex;
    align-items: center;
    gap: 8px;
    font-weight: 700;
    font-size: 15px;
    letter-spacing: 0.06em;
    text-transform: uppercase;
    color: var(--ink);
  }
  .brand__mark {
    width: 14px; height: 14px;
    border: 2px solid var(--ink);
  }
  .postcard--front .brand { position: absolute; left: 24px; top: 28px; }

  .hero { position: absolute; inset: 0; }

  .tagline {
    position: absolute;
    right: 26px;
    bottom: 20px;
    text-align: right;
  }
  .tagline__title {
    font-weight: 900;
    font-size: 44px;
    line-height: 1;
    color: var(--olive);
  }
  .tagline__sub {
    font-size: 16px;
    font-weight: 700;
    margin-top: 4px;
  }

  .back__panel { position: absolute; inset: 0; }
  .back__headline {
    position: absolute;
    left: 28px; top: 26px;
    width: 330px;
    font-weight: 900;
    font-size: 26px;
    line-height: 1.1;
    color: var(--olive);
  }
  .back__copy {
    position: absolute;
    left: 28px; top: 168px;
    width: 345px;
    color: #fff;
    font-size: 12.5px;
    line-height: 1.35;
  }
  .back__copy p + p { margin-top: 10px; }
  .back__copy strong { font-weight: 900; }
  .back__contact {
    margin-top: 10px;
    font-size: 10.5px;
    font-weight: 700;
  }
  .disclaimer {
    position: absolute;
    left: 22px; top: 368px;
    width: 360px;
    padding: 9px 14px;
    background: var(--olive-deep);
    border-radius: 14px;
    color: var(--muted);
    font-size: 8.5px;
    line-height: 1.35;
  }
  .back__brand {
    position: absolute;
    left: 440px; top: 170px;
    width: 220px;
    display: flex;
    flex-direction: column;
    align-items: center;
    gap: 18px;
  }
  .partners { display: flex; gap: 14px; align-items: center; }
  .partner { background: #c9ccd3; }
  .partner--realty { width: 54px; height: 34px; background: var(--olive); }
  .partner--crest { width: 38px; height: 38px; border-radius: 50%; background: #8c8c8c; }
  .partner--agent { width: 50px; height: 34px; background: #34467c; }
</style>
</head>
<body>

<section class="postcard postcard--front">
  <svg class="hero" viewBox="0 0 680 453" width="680" height="453" role="img" aria-label="Photo of a large stone-fronted luxury home with landscaped lawn and driveway under blue sky">
    <defs>
      <linearGradient id="heroTone" x1="0" y1="0" x2="0" y2="1">
        <stop offset="0" stop-color="var(--sky)"/>
        <stop offset="0.55" stop-color="#8d8f98"/>
        <stop offset="1" stop-color="var(--lawn)"/>
      </linearGradient>
    </defs>
    <polygon points="0,102 680,58 680,320 0,372" fill="url(#heroTone)"/>
  </svg>
  <div class="brand"><span class="brand__mark"></span>Ashby Hollow Homes</div>
  <div class="tagline">
    <div class="tagline__title">Get noticed</div>
    <div class="tagline__sub">Your home deserves it</div>
  </div>
</section>

<section class="postcard postcard--back">
  <svg class="back__panel" viewBox="0 0 680 453" width="680" height="453" aria-hidden="true">
    <polygon points="0,150 395,140 405,453 0,453" fill="var(--olive)"/>
  </svg>
  <h2 class="back__headline">We take finding Buyers for your home very seriously.</h2>
  <div class="back__copy">
    <p>Through our unique, Ashby Hollow specific website, targeted digital marketing, EXCLUSIVE Buyer incentives and our featured listing promotion, your home is in front of the people that want to see it. People who WANT to live in Ashby Hollow.</p>
    <p>Visit <strong>ashbyhollowhomes.ca</strong> to learn more about what we do so your home can <strong>GET NOTICED</strong>. Your home deserves it.</p>
    <p class="back__contact">Colin Vasterby- PREC | Tallowin Realty LTD | 604-555-0193 | homes@vasterby.ca</p>
  </div>
  <p class="disclaimer">This communication is not intended to cause or induce breach of an existing agency agreement. Although this information has been received from sources deemed reliable, we assume no responsibility for its accuracy and without offering advice, make this submission to prior sale or lease, change in price or terms, and withdrawal without notice.</p>
  <div class="back__brand">
    <div class="brand"><span class="brand__mark"></span>Ashby Hollow Homes</div>
    <div class="partners">
      <span class="partner partner--realty"></span>
      <span class="partner partner--crest"></span>
      <span class="partner partner--agent"></span>
    </div>
  </div>
</section>

</body>
</html>
```